Business Cards

I'd like help creating business cards with the full logo "Veltrona Capital Partners" on the back of the card (navy background with white writing), and abbreviated logo "VCP" on the front. Would like to list name, title, phone number, email, and website listed on front of card. Would like to keep very simple. Front font Arial or similar.

```html
<!DOCTYPE html>
<html lang="en">
<head>
<meta charset="utf-8">
<title>Veltrona Capital Partners – Business Cards</title>
<link href="https://fonts.googleapis.com/css2?family=Manrope:wght@400;700&display=swap" rel="stylesheet">
<style>
  :root {
    --navy: #00336b;
    --white: #ffffff;
    --backdrop: #3d3d3d;
  }
  * { margin: 0; padding: 0; box-sizing: border-box; }
  html, body {
    width: 1200px;
    height: 1200px;
    overflow: hidden;
    background: var(--backdrop);
    font-family: "Manrope", Arial, sans-serif;
  }
  .card {
    position: absolute;
    left: 233px;
    width: 727px;
    height: 419px;
  }
  .card--back {
    top: 164px;
    background: var(--navy);
    display: flex;
    align-items: center;
    justify-content: center;
  }
  .card--front {
    top: 649px;
    background: var(--white);
    color: var(--navy);
  }
  .brand-name {
    color: var(--white);
    font-weight: 700;
    font-size: 32px;
    letter-spacing: 0.04em;
    text-transform: uppercase;
  }
  .brand-initials {
    position: absolute;
    left: 56px;
    top: 99px;
    width: 220px;
    height: 113px;
    display: flex;
    align-items: center;
    justify-content: center;
    font-weight: 700;
    font-size: 72px;
    letter-spacing: 0.02em;
    color: var(--navy);
  }
  .person {
    position: absolute;
    left: 363px;
    top: 96px;
  }
  .person__name {
    font-weight: 700;
    font-size: 25px;
    line-height: 1.1;
  }
  .person__title {
    font-weight: 400;
    font-size: 16.5px;
    margin-top: 3px;
  }
  .address {
    position: absolute;
    left: 363px;
    top: 209px;
    font-size: 17px;
    line-height: 23px;
    font-style: normal;
  }
  .contacts {
    position: absolute;
    left: 363px;
    top: 283px;
    display: grid;
    grid-template-columns: 55px auto;
    font-size: 16px;
    line-height: 20.5px;
  }
  .website {
    position: absolute;
    left: 56px;
    top: 339px;
    font-weight: 700;
    font-size: 22px;
  }
</style>
</head>
<body>
  <section class="card card--back">
    <div class="brand-name">Veltrona Capital Partners</div>
  </section>

  <section class="card card--front">
    <div class="brand-initials">VCP</div>

    <div class="person">
      <div class="person__name">Marco Delgado</div>
      <div class="person__title">Chief Investment Officer and Partner</div>
    </div>

    <address class="address">
      2210 West Harbor Lane<br>
      Cedar Ridge, SD 57210
    </address>

    <div class="contacts">
      <span>Office</span><span>: 877-555-0142</span>
      <span>Cell</span><span>: 214-555-0187</span>
      <span>Fax</span><span>: 469-555-0163</span>
      <span>Email</span><span>: marco.delgado@veltronacp.com</span>
    </div>

    <div class="website">veltronacp.com</div>
  </section>
</body>
</html>
```